Tin Gull Wick Co. 3x3x3 reverse tuck product box

Coconut wax candles in paint cans. Fun, unpretentious. Every label has a different design that reflects the candle scent. Eclectic but simple branding. I want to take a minimalist approach as I need one box design to work for all of my product. Since my candles are so colorful and unique, I like Black and white (like my logo) on Kraft background. No candle names on the box, just my logo and welcome message on the back of the box with pertinent info (see "must haves"). Need to reflect my brand in one box that will work with my many unique labels. Company logo is black & white. I need to fit a particular template for printing. I really like the idea of a kraft background, but it would need to be a vector as my printing company cannot print white ink on kraft boxes. I am very open to non-kraft related art if it looks great! Please see requirement document. I have uploaded some of my product so the general feel of the brand is available. One candle per box. My website is www.tingullwick.com. My website and marketing material is minimalist since my each of my products are very unique and busy. Feel free to read my product descriptions to get a feel for my brand.

Target Market(s)

18-45 year olds

Industry/Entity Type

Candles/gifts

Font styles to use
Other font styles liked:
• NOW

Colors

Designer to choose colors to be used in the design.

Requirements
Must have
• My business logo, cruelty free logo, Paraben-free logo, recyclable , and handmade in Austin, TX
Nice to have
• I've uploaded a pic with back of box text I would like to see. My company tagline is: Coconut Wax Candle Awesomeness.
Should not have
• My candle label art on the box. I have many unique labels, and I will need this box to work for all of them.

```html
<!DOCTYPE html>
<html lang="en">
<head>
<meta charset="utf-8">
<title>Tin Gull Wick Co. – Product Box</title>
<link href="https://fonts.googleapis.com/css2?family=Jost:ital,wght@0,400;0,600;1,400&display=swap" rel="stylesheet">
<style>
  :root {
    --page: #ffffff;
    --stage: #d4d4d4;
    --box: #f7f7f7;
    --fold: #e6e6e6;
    --ink: #111111;
  }
  * { margin: 0; padding: 0; box-sizing: border-box; }
  html, body { width: 1200px; height: 1000px; overflow: hidden; background: var(--page); }
  body { position: relative; font-family: "Jost", sans-serif; color: var(--ink); }

  .view { position: absolute; top: 82px; width: 568px; height: 718px; background: var(--stage); }
  .view--front { left: 0; width: 617px; }
  .view--rear { left: 632px; }
  .view-caption { position: absolute; top: 822px; font-size: 22px; letter-spacing: .5px; text-align: center; width: 300px; }
  .view-caption--front { left: 183px; }
  .view-caption--rear { left: 766px; }

  .face { position: absolute; width: 240px; height: 240px; background: var(--box); border: 1px solid var(--fold);
          display: flex; align-items: center; justify-content: center; }
  .face--top { background: #fbfbfb; }
  .face--side { background: var(--fold); }

  .logo { display: flex; align-items: center; gap: 8px; font-size: 20px; font-weight: 400; white-space: nowrap; }
  .logo-mark { width: 18px; height: 18px; border: 1.5px solid var(--ink); }
  .logo--small { font-size: 16px; }
  .logo--flip { transform: rotate(180deg); }

  .welcome { flex-direction: column; gap: 12px; padding: 16px; text-align: center; }
  .welcome-bubble { width: 48px; height: 48px; }
  .welcome-text { font-weight: 600; font-size: 11.5px; line-height: 1.3; text-transform: uppercase; }

  .tagline { transform: rotate(-90deg); font-style: italic; font-size: 14px; white-space: nowrap; }

  .rear-info { flex-direction: column; gap: 10px; }
  .rear-rule { width: 180px; border-top: 1px dotted var(--ink); }
  .badges { display: flex; gap: 14px; align-items: center; }
  .badge { background: var(--ink); }
  .badge--recycle { width: 30px; height: 30px; border-radius: 50%; }
  .badge--cruelty { width: 38px; height: 26px; border-radius: 6px; }
  .badge--paraben { width: 72px; height: 28px; border-radius: 3px; }

  .origin { transform: rotate(-90deg); display: flex; align-items: center; gap: 8px; white-space: nowrap;
            font-size: 13px; letter-spacing: 1px; text-transform: uppercase; }
  .origin-state { width: 32px; height: 32px; background: var(--ink); }
</style>
</head>
<body>

<section class="view view--front">
  <div class="face face--top" style="left:288px; top:60px;">
    <div class="logo logo--small">tin gull wick co. <span class="logo-mark"></span></div>
  </div>
  <div class="face face--side" style="left:48px; top:300px;">
    <p class="tagline">Coconut Wax Candle Awesomeness.</p>
  </div>
  <div class="face welcome" style="left:288px; top:300px;">
    <svg class="welcome-bubble" viewBox="0 0 48 48" aria-hidden="true">
      <path d="M24 4a19 19 0 1 1-10 35l-8 5 3-9A19 19 0 0 1 24 4z" fill="none" stroke="#111" stroke-width="2.5"/>
      <text x="24" y="29" text-anchor="middle" font-family="Jost, sans-serif" font-size="15" font-weight="600" fill="#111">HI</text>
    </svg>
    <p class="welcome-text">I'm your awesome new Tin Gull Wick candle. You obviously have excellent taste and a great sense of humor. Keep it up. The world needs more people like you.</p>
    <div class="logo">tin gull wick co. <span class="logo-mark"></span></div>
  </div>
</section>
<p class="view-caption view-caption--front">FRONT VIEW</p>

<section class="view view--rear">
  <div class="face face--top" style="left:50px; top:60px;">
    <div class="logo logo--small logo--flip">tin gull wick co. <span class="logo-mark"></span></div>
  </div>
  <div class="face rear-info" style="left:50px; top:300px;">
    <div class="logo logo--small">tin gull wick co. <span class="logo-mark"></span></div>
    <div class="rear-rule"></div>
    <div class="badges">
      <span class="badge badge--recycle" role="img" aria-label="Recyclable badge"></span>
      <span class="badge badge--cruelty" role="img" aria-label="Cruelty free badge"></span>
      <span class="badge badge--paraben" role="img" aria-label="Paraben free badge"></span>
    </div>
  </div>
  <div class="face face--side" style="left:290px; top:300px;">
    <p class="origin">Handmade in <span class="origin-state" role="img" aria-label="Texas state silhouette"></span> Austin, TX Y'all</p>
  </div>
</section>
<p class="view-caption view-caption--rear">REAR VIEW</p>

</body>
</html>
```